High-end residential home builder needs a business card design

We need a new business card design for a small residential construction company based in Boise, Idaho. We specialize in building custom high-end homes and remodels, with a focus on great design and craftsmanship.

We would like to use our current logo, but open to new color suggestions.
Just looking for a clean, sharp, modern design that looks high-end.

Target Market(s)

Upscale clientele

Industry/Entity Type

Contractor

Contact Information for Business Card

Company: Stonefield Custom Builders
Name: Marcus Tilley
Phone number: 208 367 4120
Email: MarcusTilleySCB@mailbox-example.com
Website: Stonefieldcustombuilders-example.com

Font styles to use
Serif
Sans Serif

Requirements
Must have
• Company Logo
Company name
My name
My phone number
My email
Company website
Nice to have
• I have attached a few photos of cards that I really like.

```html
<!DOCTYPE html>
<html lang="en">
<head>
<meta charset="utf-8">
<title>Stonefield Custom Builders – Business Card</title>
<link rel="stylesheet" href="https://fonts.googleapis.com/css2?family=Montserrat:wght@500;600;700&family=Poppins:wght@400;500&display=swap">
<style>
  :root {
    --stage: #1f1f1f;
    --card-white: #ffffff;
    --ink: #2a1a10;
    --copper: #e08a2c;
    --copper-light: #cf7a2e;
    --umber: #3b210f;
    --ghost: #ededed;
  }
  * { box-sizing: border-box; margin: 0; padding: 0; }
  html, body {
    width: 1200px; height: 900px; overflow: hidden;
    background: var(--stage);
  }
  .stage { position: relative; width: 1200px; height: 900px; }

  .card {
    position: absolute;
    width: 640px; height: 366px;
    border-radius: 22px;
    overflow: hidden;
  }

  /* Back face */
  .card-back {
    left: 110px; top: 60px;
    background: linear-gradient(200deg, var(--copper-light) 0%, #8a4d1f 45%, var(--umber) 100%);
  }
  .card-back .pattern-field { position: absolute; inset: 0; }
  .back-brand {
    position: absolute; inset: 0;
    display: flex; align-items: center; justify-content: center; gap: 14px;
    font-family: "Montserrat", sans-serif; font-weight: 600;
    font-size: 22px; letter-spacing: 0.32em; color: #ffffff;
  }
  .back-brand .brand-square {
    width: 16px; height: 16px; background: #ffffff;
  }

  /* Front face */
  .card-front {
    left: 450px; top: 474px;
    background: var(--card-white);
  }
  .ghost-name {
    position: absolute; right: 40px; top: 26px;
    font-family: "Montserrat", sans-serif; font-weight: 700;
    font-size: 58px; letter-spacing: 0.06em; color: var(--ghost);
  }
  .brand {
    position: absolute; left: 42px; top: 58px;
    display: flex; align-items: flex-start; gap: 14px;
  }
  .brand-square {
    width: 18px; height: 18px; background: var(--ink); margin-top: 4px;
  }
  .brand-name {
    font-family: "Montserrat", sans-serif; font-weight: 600;
    font-size: 21px; line-height: 1.45; letter-spacing: 0.3em;
    color: var(--ink);
  }
  .contact {
    position: absolute; right: 34px; top: 128px;
    list-style: none;
    font-family: "Poppins", sans-serif; font-size: 13.5px; color: var(--ink);
    text-align: right;
  }
  .contact li {
    display: flex; align-items: center; justify-content: flex-end; gap: 10px;
    height: 22px;
  }
  .contact svg { width: 14px; height: 14px; flex: none; }
  .divider {
    position: absolute; left: 42px; right: 34px; top: 214px;
    height: 1px; background: var(--ink);
  }
  .person {
    position: absolute; left: 42px; top: 236px;
    font-family: "Montserrat", sans-serif;
  }
  .person-name {
    font-weight: 700; font-size: 27px; color: var(--ink); letter-spacing: 0.01em;
  }
  .person-role {
    font-weight: 600; font-size: 17px; color: var(--copper); letter-spacing: 0.02em;
  }
  .base-rule {
    position: absolute; left: 0; right: 0; bottom: 22px;
    height: 2px; background: var(--copper);
  }
</style>
</head>
<body>
<main class="stage">

  <section class="card card-back" aria-label="Card back">
    <svg class="pattern-field" role="img" aria-label="Repeating hexagon monogram pattern over copper gradient" viewBox="0 0 640 366" preserveAspectRatio="none">
      <rect width="640" height="366" fill="none"/>
    </svg>
    <div class="back-brand"><span class="brand-square"></span>STONEFIELD</div>
  </section>

  <section class="card card-front" aria-label="Card front">
    <div class="ghost-name" aria-hidden="true">STONEFIELD</div>

    <div class="brand">
      <span class="brand-square"></span>
      <p class="brand-name">STONEFIELD<br>CUSTOM BUILDERS</p>
    </div>

    <ul class="contact">
      <li>208 367 4120
        <svg viewBox="0 0 24 24" fill="var(--copper)"><path d="M6.6 10.8a15.1 15.1 0 0 0 6.6 6.6l2.2-2.2c.3-.3.7-.4 1-.2 1.1.4 2.3.6 3.6.6.6 0 1 .4 1 1V20c0 .6-.4 1-1 1A17 17 0 0 1 3 4c0-.6.4-1 1-1h3.5c.6 0 1 .4 1 1 0 1.3.2 2.5.6 3.6.1.3 0 .7-.2 1z"/></svg>
      </li>
      <li>MarcusTilleySCB@mailbox-example.com
        <svg viewBox="0 0 24 24" fill="var(--copper)"><path d="M2 5h20v14H2z"/><path d="M2 5l10 8 10-8" fill="none" stroke="#fff" stroke-width="1.6"/></svg>
      </li>
      <li>www.stonefieldcustombuilders-example.com
        <svg viewBox="0 0 24 24" fill="none" stroke="var(--copper)" stroke-width="2"><circle cx="12" cy="12" r="9"/><path d="M3 12h18M12 3c3 3 3 15 0 18M12 3c-3 3-3 15 0 18"/></svg>
      </li>
    </ul>

    <div class="divider"></div>

    <div class="person">
      <p class="person-name">MARCUS TILLEY</p>
      <p class="person-role">MANAGING DIRECTOR</p>
    </div>

    <div class="base-rule"></div>
  </section>

</main>
</body>
</html>
```